Lawn care business card

I am looking for a quality designed personal business card to represent the quality and elegant nature of our company. We separate ourselves in our market by the aesthetic value of our work, so I am looking for marketing material that does the same. We target our marketing high end customers, and we try to avoid price shoppers. I am open to all design options, so long as they are in line with our companies values.

We are tend to go with a retro look on everything from our logo and print material, to our uniforms. We like to portray and "old fashion" set of core values, with a modern elegance. So a wild and crazy look is out of the question.

Things I'd like on the card:
1.) Logo
2.) Phone number: (816) 555-0193
3.) Website: Verdanthollow.com
4.) Email: peterwalsh@verdanthollow.com
5.) My name: Peter Walsh
6.) Facebook link: facebook.com/GreenridgeLawnandLandscape
7.) Instagram: http://instagram.com/verdanthollow

Attached is a copy of our logo.

```html
<!DOCTYPE html>
<html lang="en">
<head>
<meta charset="utf-8">
<title>Verdant Hollow – Business Card</title>
<link rel="stylesheet" href="https://fonts.googleapis.com/css2?family=Bevan&family=Arimo:wght@700&family=Archivo+Black&display=swap">
<style>
  :root {
    --backdrop: #e4e4e4;
    --card: #ffffff;
    --orange: #e8522a;
    --orange-soft: #f2a07e;
    --charcoal: #202426;
    --tan: #e2c49a;
    --ink: #111111;
  }
  * { margin: 0; padding: 0; box-sizing: border-box; }
  html, body {
    width: 1200px; height: 675px; overflow: hidden;
    background: var(--backdrop);
  }
  .card {
    position: absolute; left: 75px; top: 38px;
    width: 1050px; height: 600px;
    background: var(--card);
    overflow: hidden;
    box-shadow: 0 4px 14px rgba(0,0,0,0.18);
  }
  .card-shapes { position: absolute; inset: 0; }
  .brand {
    position: absolute; left: 96px; top: 180px;
    display: flex; align-items: center; gap: 10px;
  }
  .brand-dot {
    width: 30px; height: 30px; border-radius: 50%;
    background: var(--orange);
  }
  .brand-name {
    font-family: "Arimo", Arial, sans-serif; font-weight: 700;
    font-size: 21px; color: var(--charcoal);
    letter-spacing: 1px; text-transform: uppercase;
    white-space: nowrap;
  }
  .holder-name {
    position: absolute; left: 385px; top: 166px;
    font-family: "Bevan", Georgia, serif; font-weight: 400;
    font-size: 42px; line-height: 1.1; color: var(--orange);
    white-space: nowrap;
  }
  .contacts {
    position: absolute; left: 350px; top: 252px;
    list-style: none;
  }
  .contacts li {
    display: flex; align-items: center; gap: 40px;
    height: 44px;
    font-family: "Arimo", Arial, sans-serif; font-weight: 700;
    font-size: 20px; color: var(--ink);
    white-space: nowrap;
  }
  .contacts .phone-number {
    font-family: "Archivo Black", Arial, sans-serif; font-weight: 400;
    font-size: 21px; letter-spacing: 1px;
  }
  .contact-icon { width: 34px; height: 34px; flex: none; }
  .website {
    position: absolute; left: 0; right: 0; top: 515px;
    text-align: center;
    font-family: "Bevan", Georgia, serif;
    font-size: 25px; letter-spacing: 9px; color: #ffffff;
  }
</style>
</head>
<body>
  <main class="card">
    <svg class="card-shapes" width="1050" height="600" viewBox="0 0 1050 600">
      <circle class="burst-decoration" role="img" aria-label="Orange dotted sunburst ornament" cx="978" cy="105" r="160" fill="var(--orange)" opacity="0.85"/>
      <circle class="ring-decoration" role="img" aria-label="Black and orange dotted ring ornament" cx="45" cy="410" r="140" fill="var(--charcoal)"/>
      <polygon class="accent-stripe" points="0,472 1050,432 1050,446 0,492" fill="var(--orange)"/>
      <polygon class="footer-band" points="0,488 1050,444 1050,600 0,600" fill="var(--charcoal)"/>
    </svg>

    <div class="brand">
      <span class="brand-dot"></span>
      <span class="brand-name">Verdant Hollow</span>
    </div>

    <h1 class="holder-name">Peter Walsh</h1>

    <ul class="contacts">
      <li>
        <svg class="contact-icon" viewBox="0 0 36 36" aria-hidden="true">
          <rect width="36" height="36" rx="5" fill="var(--tan)"/>
          <path d="M9 14c0-4 18-4 18 0v3h-5v-3h-8v3H9z" fill="#fff"/>
          <rect x="11" y="19" width="14" height="9" rx="2" fill="#fff"/>
        </svg>
        <span class="phone-number">(816) 555-0193</span>
      </li>
      <li>
        <svg class="contact-icon" viewBox="0 0 36 36" aria-hidden="true">
          <rect width="36" height="36" rx="5" fill="var(--tan)"/>
          <rect x="7" y="10" width="22" height="16" fill="#fff"/>
          <path d="M7 10l11 9 11-9" fill="none" stroke="var(--tan)" stroke-width="2"/>
        </svg>
        <span>peterwalsh@verdanthollow.com</span>
      </li>
      <li>
        <svg class="contact-icon" viewBox="0 0 36 36" aria-hidden="true">
          <rect width="36" height="36" rx="5" fill="var(--tan)"/>
        </svg>
        <span>facebook.com/GreenridgeLawnandLandscape</span>
      </li>
      <li>
        <svg class="contact-icon" viewBox="0 0 36 36" aria-hidden="true">
          <rect width="36" height="36" rx="5" fill="var(--tan)"/>
        </svg>
        <span>http://instagram.com/verdanthollow</span>
      </li>
    </ul>

    <p class="website">www.Verdanthollow.com</p>
  </main>
</body>
</html>
```